Brightwater Array Panel cleaning business needs a flyer designed.

I need a flyer design for a new company based in Los Angeles. We clean solar panels at an affordable price, we're insured, and licensed. we would like the design to include the colors Red, white, and Blue. The flyer should emphasize the importance of cleaning solar panels to maintain the warranty and add longevity to the solar panels.

```html
<!DOCTYPE html>
<html lang="en">
<head>
<meta charset="utf-8">
<title>Brightwater Array – Solar Panel Cleaning Flyer</title>
<link href="https://fonts.googleapis.com/css2?family=Aldrich&family=Outfit:wght@400;500;600&display=swap" rel="stylesheet">
<style>
  :root{
    --navy:#2e3592;
    --red:#dc3432;
    --red-deep:#c1222a;
    --white:#ffffff;
    --ink:#1d1d2b;
    --stage:#0d0d0d;
    --sky:#c9d3e2;
  }
  *{margin:0;padding:0;box-sizing:border-box}
  html,body{width:1200px;height:827px;overflow:hidden;background:var(--stage)}
  body{position:relative;font-family:"Outfit",sans-serif;color:var(--ink)}
  .display{font-family:"Aldrich",sans-serif;font-weight:400}

  .page{position:absolute;top:42px;width:508px;height:720px;overflow:hidden;background:var(--white)}
  .page--front{left:82px;background:var(--navy)}
  .page--back{left:643px}

  /* front */
  .brand-bar{position:absolute;left:0;top:0;width:100%;height:94px;background:var(--red-deep);display:flex;flex-direction:column;align-items:center;justify-content:center;color:var(--white)}
  .brand-bar__name{font-family:"Aldrich",sans-serif;font-size:38px;letter-spacing:3px;line-height:1}
  .brand-bar__sub{margin-top:8px;width:220px;height:3px;background:var(--white)}
  .hero-title{position:absolute;top:122px;width:100%;text-align:center;color:var(--white);font-size:32px;line-height:40px;letter-spacing:.5px}
  .tagline-band{position:absolute;top:227px;width:100%;height:43px;background:var(--red);color:var(--white);font-size:20px;display:flex;align-items:center;justify-content:center}
  .why-title{position:absolute;top:302px;width:100%;text-align:center;color:var(--white);font-size:21px}
  .photo{position:absolute;left:0;top:380px;width:100%;height:340px;background:linear-gradient(180deg,var(--navy) 0%,#8d97c6 22%,var(--sky) 45%,#e6ebf2 70%,#9aa6b8 100%)}
  .benefit{position:absolute;width:233px;height:83px;background:var(--white);border:1px solid var(--navy);display:flex;align-items:center;padding:0 10px 0 12px;gap:12px}
  .benefit svg{flex:none;width:38px;height:38px;stroke:var(--navy);fill:none;stroke-width:2;stroke-linecap:round;stroke-linejoin:round}
  .benefit h3{font-weight:500;font-size:15px;color:var(--navy);margin-bottom:3px}
  .benefit p{font-size:10.5px;line-height:12.5px;color:var(--ink)}
  .b1{left:16px;top:356px}.b2{left:259px;top:356px}.b3{left:16px;top:450px}.b4{left:259px;top:450px}

  /* back */
  .section-head{position:absolute;top:0;width:100%;height:48px;background:var(--navy);color:var(--white);font-size:24px;padding-left:17px;letter-spacing:.5px;display:flex;align-items:center}
  .services{position:absolute;top:59px;left:18px;list-style:none}
  .service{display:flex;align-items:center;height:64px}
  .service__icon{width:46px;height:46px;border-radius:50%;background:var(--red);display:flex;align-items:center;justify-content:center;flex:none}
  .service__icon svg{width:26px;height:26px;stroke:var(--white);fill:none;stroke-width:1.8;stroke-linecap:round;stroke-linejoin:round}
  .service__text{margin-left:18px}
  .service h3{font-family:"Aldrich",sans-serif;font-weight:400;font-size:16px;color:var(--navy);line-height:22px}
  .service p{font-size:16px;line-height:22px;color:var(--ink)}
  .choose{position:absolute;top:394px;width:100%;height:175px;background:var(--navy);color:var(--white)}
  .choose h2{font-family:"Aldrich",sans-serif;font-weight:400;font-size:24px;padding:20px 0 0 18px;line-height:1}
  .reasons{position:absolute;top:64px;left:0;width:100%;display:flex}
  .reason{height:88px;padding-left:18px}
  .reason + .reason{border-left:1.5px solid var(--white);padding-left:26px}
  .reason svg{width:28px;height:28px;stroke:var(--white);fill:none;stroke-width:1.6;stroke-linecap:round;stroke-linejoin:round}
  .reason p{font-size:12.5px;line-height:15.5px;margin-top:10px;font-weight:500}
  .r1{width:132px}.r2{width:141px}.r3{width:125px}.r4{width:110px}
  .cta{position:absolute;top:569px;width:100%;height:56px;background:var(--red);color:var(--white);font-family:"Aldrich",sans-serif;font-size:24px;display:flex;align-items:center;justify-content:center;letter-spacing:.5px}
  .contact{position:absolute;top:625px;width:100%;height:95px;display:flex}
  .contact__brand{width:286px;flex:none;border-right:1.5px solid var(--navy);text-align:center;padding-top:14px}
  .contact__name{font-family:"Aldrich",sans-serif;font-size:21px;color:var(--navy);letter-spacing:1px}
  .contact__slogan{font-size:12.8px;margin-top:8px}
  .contact__address{font-size:12.5px;color:var(--navy);margin-top:10px}
  .contact__call{padding:14px 0 0 14px}
  .contact__label{font-size:13px;font-weight:600;color:var(--navy)}
  .contact__phone{font-family:"Aldrich",sans-serif;font-size:25.5px;color:var(--red);margin-top:1px;white-space:nowrap}
  .contact__web{font-family:"Aldrich",sans-serif;font-size:14px;color:var(--navy);margin-top:3px}
</style>
</head>
<body>

<section class="page page--front">
  <header class="brand-bar">
    <div class="brand-bar__name">BRIGHTWATER ARRAY</div>
    <div class="brand-bar__sub"></div>
  </header>
  <h1 class="hero-title display">PREMIUM SOLAR PANEL<br>CLEANING SERVICES</h1>
  <div class="tagline-band">Maximize Your Energy Output &amp; Savings!</div>
  <h2 class="why-title display">Why Clean Your Solar Panels?</h2>
  <div class="photo" role="img" aria-label="Workers in hard hats and safety vests cleaning rooftop solar panels under a cloudy sky"></div>

  <article class="benefit b1">
    <svg viewBox="0 0 40 40"><path d="M6 28a14 14 0 1 1 28 0"/><path d="M20 26l9-6"/><circle cx="20" cy="26" r="2.5"/></svg>
    <div><h3>Boost Efficiency</h3><p>Dirt, dust, and debris reduce energy production by up to 30%</p></div>
  </article>
  <article class="benefit b2">
    <svg viewBox="0 0 40 40"><path d="M11 5h18M11 35h18M13 5c0 10 14 10 14 15s-14 5-14 15M27 5c0 10-14 10-14 15s14 5 14 15"/></svg>
    <div><h3>Extend Lifespan</h3><p>Keeps your panel warranty valid and adds years of performance</p></div>
  </article>
  <article class="benefit b3">
    <svg viewBox="0 0 40 40"><ellipse cx="19" cy="25" rx="13" ry="9"/><path d="M10 32v4M26 32v4M32 23h3"/><circle cx="20" cy="9" r="5"/></svg>
    <div><h3>Save Money</h3><p>More energy means lower electricity bills</p></div>
  </article>
  <article class="benefit b4">
    <svg viewBox="0 0 40 40"><circle cx="21" cy="17" r="9"/><path d="M21 8V3M21 3c-3-2-6-1-7 1M21 3c3-2 6-1 7 1M3 30l7-4h10l-4 4h8l10-8"/></svg>
    <div><h3>Eco-Friendly Cleaning</h3><p>Safe, non-abrasive, and chemical-free methods</p></div>
  </article>
</section>

<section class="page page--back">
  <h2 class="section-head display">OUR SERVICES</h2>
  <ul class="services">
    <li class="service">
      <span class="service__icon"><svg viewBox="0 0 26 26"><path d="M4 12h18v10H4zM4 17h18M10 12v10M16 12v10"/><circle cx="13" cy="7" r="2.5"/></svg></span>
      <div class="service__text"><h3>Deep Solar Panel Cleaning</h3><p>Removes dust, bird droppings, and grime</p></div>
    </li>
    <li class="service">
      <span class="service__icon"><svg viewBox="0 0 26 26"><path d="M4 22L18 8M8 4l14 14M18 8l2-4 2 2-4 2M4 22l-1-1"/></svg></span>
      <div class="service__text"><h3>Regular Maintenance Plans</h3><p>Monthly, quarterly, or annual service options</p></div>
    </li>
    <li class="service">
      <span class="service__icon"><svg viewBox="0 0 26 26"><path d="M5 4h13v18H5zM8 9h7M8 13h4"/><circle cx="17" cy="17" r="3.5"/><path d="M20 20l3 3"/></svg></span>
      <div class="service__text"><h3>Inspection &amp; Performance Check</h3><p>Helps keep your manufacturer warranty valid</p></div>
    </li>
    <li class="service">
      <span class="service__icon"><svg viewBox="0 0 26 26"><path d="M4 6h14v16H4z"/><circle cx="8" cy="11" r="1"/><circle cx="12" cy="15" r="1"/><path d="M19 12l5 9h-10z"/></svg></span>
      <div class="service__text"><h3>Hard Water Stain Removal</h3><p>Prevents long-term damage from mineral buildup</p></div>
    </li>
    <li class="service">
      <span class="service__icon"><svg viewBox="0 0 26 26"><path d="M6 3h14v20H6zM9 7h3v3H9zM14 7h3v3h-3zM9 12h3v3H9zM14 12h3v3h-3zM11 23v-4h4v4"/></svg></span>
      <div class="service__text"><h3>Commercial &amp; Residential Services</h3><p>Custom plans for homes, businesses &amp; solar farms</p></div>
    </li>
  </ul>

  <section class="choose">
    <h2>WHY CHOOSE US?</h2>
    <div class="reasons">
      <div class="reason r1">
        <svg viewBox="0 0 28 28"><circle cx="14" cy="7" r="3"/><circle cx="6" cy="10" r="2.5"/><circle cx="22" cy="10" r="2.5"/><path d="M9 24v-7a5 5 0 0 1 10 0v7zM2 24v-5a4 4 0 0 1 6-3M26 24v-5a4 4 0 0 0-6-3M2 24h24"/></svg>
        <p>Licensed &amp;<br>Insured<br>Professionals</p>
      </div>
      <div class="reason r2">
        <svg viewBox="0 0 28 28"><path d="M8 16V6a2 2 0 0 1 4 0v6M12 5a2 2 0 0 1 4 0v7M16 6a2 2 0 0 1 4 0v5M8 16l-3-3a2 2 0 0 0-3 3l6 8h6"/><path d="M18 15l6 2v4c0 3-3 5-6 6-3-1-6-3-6-6v-4z"/></svg>
        <p>Eco-Friendly &amp;<br>Safe Cleaning<br>Techniques</p>
      </div>
      <div class="reason r3">
        <svg viewBox="0 0 28 28"><circle cx="17" cy="8" r="6"/><path d="M17 5v6M2 20h5l4 2h8l7-5-2-2-6 3h-5M7 18l3-2h6"/></svg>
        <p>Affordable &amp;<br>Flexible<br>Pricing</p>
      </div>
      <div class="reason r4">
        <svg viewBox="0 0 28 28"><path d="M14 2l1.5 3 3 .5-2 2 .5 3-3-1.5-3 1.5.5-3-2-2 3-.5zM5 6l1 2 2 .3-1.5 1.5.3 2L5 11l-1.8.8.3-2L2 8.3 4 8zM23 6l1 2 2 .3-1.5 1.5.3 2-1.8-.8-1.8.8.3-2L20 8.3 22 8z"/><path d="M8 26v-9h4l3-5a2 2 0 0 1 3 2l-1 3h5l-2 9z"/></svg>
        <p>100%<br>Satisfaction<br>Guarantee</p>
      </div>
    </div>
  </section>

  <div class="cta">CALL NOW FOR A FREE QUOTE!</div>

  <footer class="contact">
    <div class="contact__brand">
      <div class="contact__name">BRIGHTWATER ARRAY</div>
      <p class="contact__slogan">Powering Your Panels for Maximum Efficiency!</p>
      <p class="contact__address">410 Harbor Light Road, Los Angeles, CA 90017</p>
    </div>
    <div class="contact__call">
      <div class="contact__label">CALL US</div>
      <div class="contact__phone">(555) 014 2290</div>
      <div class="contact__web">www.brightwaterarray.com</div>
    </div>
  </footer>
</section>

</body>
</html>
```